Maple Ridge Rally 21 day Challenge

We are having a Maple Ridge Rally Challenge at our fitness studio. We need a poster design using the template attached as a reference. I have also included our Brovalune logo to put on the poster. Please DO NOT use the graphics in the flyer as we are expecting something much better :-)

-Size needed 11x17 with bleeding for printing

-We need this made in Photoshop (CS3 friendly) or at least delivered in PS as we might change some text or re-arrange the design later on.

-We need this in layers.

Fitness

```html
<!DOCTYPE html>
<html lang="en">
<head>
<meta charset="utf-8">
<title>Maple Ridge Rally Challenge Poster</title>
<link href="https://fonts.googleapis.com/css2?family=Anton&family=Fira+Sans+Extra+Condensed:wght@500;600;700;800&display=swap" rel="stylesheet">
<style>
  :root{
    --backdrop:#9a9a9a;
    --sky:#c9dbe8;
    --sky-low:#bcd3e3;
    --sea:#5fa6b5;
    --sea-light:#8cc4c8;
    --sand:#ece6dc;
    --teal:#1a949c;
    --ink:#222222;
    --red:#e8323c;
    --yellow:#fff200;
    --white:#ffffff;
  }
  *{box-sizing:border-box;margin:0;padding:0}
  html,body{width:1182px;height:1200px;overflow:hidden;background:var(--backdrop)}
  .poster{
    position:absolute;left:219px;top:25px;width:744px;height:1150px;overflow:hidden;
    font-family:"Fira Sans Extra Condensed",sans-serif;
    box-shadow:0 18px 30px rgba(0,0,0,.35);
  }
  .beach-photo{
    position:absolute;inset:0;
    background:linear-gradient(180deg,var(--sky) 0%,var(--sky-low) 54%,var(--sea) 54.5%,var(--sea-light) 66%,#d9ecea 74%,var(--sand) 86%,var(--sand) 100%);
  }
  .headline{
    position:absolute;left:0;right:0;top:74px;text-align:center;
    font-family:"Anton",sans-serif;color:var(--teal);text-transform:uppercase;
    line-height:.92;letter-spacing:-1px;
  }
  .headline .line-one{display:block;font-size:86px}
  .headline .line-two{display:block;font-size:86px}
  .banner{position:absolute;height:36px;color:var(--white);font-weight:700;font-size:36px;line-height:36px;text-align:center;text-transform:uppercase;white-space:nowrap}
  .banner.one{left:196px;width:417px;top:254px;background:var(--ink)}
  .banner.two{left:128px;width:476px;top:291px;background:var(--red)}
  .banner.three{left:240px;width:318px;top:328px;background:var(--ink)}
  .feature{position:absolute;padding:14px 12px 0 17px;font-weight:600;font-size:17px;line-height:23px}
  .feature.light{background:var(--white);color:var(--ink)}
  .feature.dark{background:var(--ink);color:var(--white)}
  .feature .num{
    position:absolute;left:-17px;top:-16px;width:30px;height:30px;border-radius:50%;
    background:var(--yellow);border:2px solid var(--white);color:var(--ink);
    font-weight:800;font-size:19px;line-height:26px;text-align:center;
  }
  .f1{left:75px;top:390px;width:165px;height:167px}
  .f2{left:264px;top:431px;width:116px;height:168px}
  .f3{left:404px;top:390px;width:139px;height:167px}
  .f4{left:565px;top:431px;width:144px;height:168px}
  .price{
    position:absolute;left:262px;top:684px;width:202px;height:202px;border-radius:50%;
    background:var(--yellow);border:4px solid var(--white);text-align:center;
    padding-top:26px;color:var(--ink);font-weight:700;font-size:23px;line-height:22px;letter-spacing:-.5px;
  }
  .price .amount{display:block;font-family:"Anton",sans-serif;color:var(--red);font-size:56px;line-height:60px;margin-top:2px}
  .footer-band{position:absolute;left:0;right:0;top:916px;bottom:0;background:rgba(255,255,255,.72)}
  .testimonial{
    position:absolute;left:114px;top:950px;width:156px;height:156px;border-radius:50%;background:var(--yellow);
    padding:36px 0 0 34px;font-weight:700;font-size:14px;line-height:18px;color:var(--ink);
  }
  .testimonial .author{display:block;font-size:10px;line-height:14px}
  .quote-mark{position:absolute;font-family:"Anton",sans-serif;font-size:120px;line-height:1;color:#333}
  .quote-mark.open{left:92px;top:916px}
  .quote-mark.close{left:232px;top:1034px}
  .divider{position:absolute;left:313px;top:932px;width:1px;height:193px;background:#444}
  .brand{
    position:absolute;left:333px;top:934px;width:287px;height:97px;background:var(--white);border:4px solid var(--ink);
    display:flex;align-items:center;justify-content:center;gap:12px;
    font-weight:800;font-size:46px;color:var(--ink);letter-spacing:1px;
  }
  .brand .mark{width:22px;height:22px;background:var(--teal)}
  .cta{position:absolute;left:333px;top:1040px;font-weight:700;font-size:23px;line-height:19px;color:var(--ink);text-transform:uppercase}
  .cta .hot{color:var(--red)}
  .cta .contact{display:block;color:var(--red);font-size:27px;line-height:26px;margin-top:6px}
</style>
</head>
<body>
<div class="poster">
  <div class="beach-photo" role="img" aria-label="Photo of a smiling couple in swimwear holding hands on a sunny beach, sea and pale sky behind"></div>

  <h1 class="headline"><span class="line-one">Maple Ridge</span><span class="line-two">Rally</span></h1>

  <div class="banner one">Discover the secret</div>
  <div class="banner two">to a beach-ready body</div>
  <div class="banner three">in just 21 days!</div>

  <div class="feature light f1"><span class="num">1</span>9 total training sessions designed to incinerate fat off your midsection, thighs, and arms</div>
  <div class="feature dark f2"><span class="num">2</span>21 days of nutritional guidance, including delicious recipes</div>
  <div class="feature light f3"><span class="num">3</span>A Success Session to map out your individual plan for success</div>
  <div class="feature dark f4"><span class="num">4</span>Your very own Personal Accountability Coach to ensure you get results</div>

  <div class="price">You get<br>all this -<br>a $399 value -<br>for ONLY<span class="amount">$99!</span></div>

  <div class="footer-band"></div>
  <div class="testimonial">I've never<br>been more fit<br>in my life-<br>at age 41!<span class="author">-Dana Whitcomb</span></div>
  <div class="quote-mark open">&ldquo;</div>
  <div class="quote-mark close">&rdquo;</div>

  <div class="divider"></div>
  <div class="brand"><span class="mark"></span>BROVALUNE</div>
  <div class="cta"><span class="hot">Hurry!</span> Space is limited to only<br>20 participants!!!<br>Claim your spot now:<span class="contact">Website and phone number</span></div>
</div>
</body>
</html>
```